Bubble-Diagramm als Infografik für unseren Kunden aus der Immobilienbranche
Zielgruppe
Wir sind ein Software-Unternehmen mit Kunden aus allen Branchen. Ganz generell für unsere Homepage, konkret aber auch im Rahmen eines Kundenprojektes suchen wir ansprechende Beispiele und kreative Visualisierungen, wie Diagramme zu bestimmten Sachverhalten dargestellt werden können.
Aufgabenstellung
Wir möchten die Möglichkeiten darstellen, mit excelbasierten Diagrammtypen den gewissen „Wow-Effekt“ bei unseren Kunden hervorzurufen. Konkret geht es uns hier um die Erstellung eines Bubble-Diagramms. In einem Objektvergleich von Gewerbeimmobilien sollen drei Dimensionen (hier: Größe des Objekte, Gesamtmiete über die Laufzeit, effektive Miete je Quadratmeter) im Bubble-Diagramm dargestellt werden. Siehe hierzu Entwurf (.xls-Datei) anbei.
Eine Orientierung an unserem Firmenlayout (www.brenolux-net.de) ist ausdrücklich erwünscht. Die Grafik sollte aufgeräumt und klar wirken, ohne nüchtern zu sein, um auf der einen Seite mit der Form nicht vom Inhalt abzulenken, und sich auf der anderen Seite aber eben doch über die Form von der Konkurrenz, die nur mit Excel-Bordmitteln arbeitet, erkennbar abzuheben. Denkbar sind grundsätzlich auch Piktogramme oder vergleichbare, Inhalt transportierende Elemente im Graphik-Hintergrund oder in der Umrahmung, immer unter der Maßgabe, dass sie nicht zu verspielt daherkommen.
Technisch sind wir in der Lage, Excel-Diagramme auch „interaktiv“ zu gestalten, also nach Klick auf ein Diagrammelement ein Kontextmenü oder erweiterte Informationen einzublenden. Daher wünschen wir uns als Teil des Entwurfs, beispielhaft für eine Blase, die Darstellung so eines interaktiven Elements: eines Kontextmenüs / und oder eines Datenblatts.
Vorzugsweise soll die Grafik im Excel-Format zur Verfügung gestellt werden, das ist aber kein Must-have.

```html
<!DOCTYPE html>
<html lang="de">
<head>
<meta charset="utf-8">
<title>Objektvergleich – Bubble-Diagramm</title>
<link rel="stylesheet" href="https://fonts.googleapis.com/css2?family=Lora:wght@400;500;600&family=Nunito:wght@800&display=swap">
<style>
  :root {
    --page: #d4d4d8;
    --sheet: #f1f1fb;
    --ink: #0b2f9f;
    --axis: #c9c7f6;
    --grid: #d3d1f5;
    --bubble: #c9c8f7;
    --bubble-soft: #dcdbfa;
    --arrow: #b9b4ad;
    --scenery: #e6e4ec;
  }
  * { margin: 0; padding: 0; box-sizing: border-box; }
  html, body { width: 900px; height: 1200px; overflow: hidden; background: var(--page); }
  .canvas { position: relative; width: 900px; height: 1200px; }
  .chart-sheet {
    position: absolute; left: 0; top: 347px; width: 900px; height: 506px;
    background: radial-gradient(ellipse at 45% 40%, #ffffff 0%, var(--sheet) 70%);
  }
  .chart-sheet svg { display: block; width: 900px; height: 506px; }
  .serif { font-family: "Lora", Georgia, serif; fill: var(--ink); }
  .axis-value { font-size: 13px; }
  .axis-unit { font-size: 8px; }
  .axis-title { font-size: 17px; font-weight: 500; }
  .legend-text { font-size: 12px; }
  .info-title { font-size: 15px; }
  .info-text { font-size: 10.5px; }
  .bubble-number { font-family: "Nunito", Arial, sans-serif; font-weight: 800; font-size: 25px; fill: var(--ink); }
  .bubble-ring { fill: none; stroke: var(--ink); stroke-width: 4; stroke-linecap: round; stroke-dasharray: 85 15; stroke-dashoffset: -70; }
  .bubble-fill { fill: var(--bubble); }
  .trend-arrow { fill: none; stroke: var(--arrow); stroke-width: 4; stroke-linecap: round; }
</style>
</head>
<body>
<div class="canvas">
  <div class="chart-sheet">
    <svg viewBox="0 0 900 506" xmlns="http://www.w3.org/2000/svg">
      <defs>
        <marker id="arrow-head" viewBox="0 0 10 10" refX="5" refY="5" markerWidth="3" markerHeight="3" orient="auto">
          <path d="M0,0 L10,5 L0,10 z" fill="var(--arrow)"/>
        </marker>
        <linearGradient id="info-fill" x1="0" y1="0" x2="1" y2="1">
          <stop offset="0" stop-color="#bdbcf4"/>
          <stop offset="1" stop-color="#d8d7fa"/>
        </linearGradient>
      </defs>

      <!-- background scenery -->
      <rect class="scenery" role="img" aria-label="Blasse Strichzeichnung einer Stadtsilhouette mit Baum und Fahrrad" x="167" y="145" width="613" height="250" rx="4" fill="var(--scenery)" opacity="0.55"/>

      <!-- grid -->
      <line x1="152" y1="219" x2="795" y2="219" stroke="var(--grid)" stroke-width="1.5"/>
      <line x1="464" y1="40" x2="464" y2="403" stroke="var(--grid)" stroke-width="1.5"/>
      <line x1="152" y1="447" x2="152" y2="425" stroke="var(--grid)" stroke-width="1"/>
      <line x1="795" y1="447" x2="795" y2="425" stroke="var(--grid)" stroke-width="1"/>

      <!-- axes -->
      <line x1="152" y1="403" x2="152" y2="43" stroke="var(--axis)" stroke-width="4" stroke-linecap="round"/>
      <path d="M145,52 L152,40 L159,52" fill="none" stroke="var(--axis)" stroke-width="4" stroke-linecap="round" stroke-linejoin="round"/>
      <line x1="152" y1="403" x2="795" y2="403" stroke="var(--axis)" stroke-width="4" stroke-linecap="round"/>
      <path d="M786,396 L798,403 L786,410" fill="none" stroke="var(--axis)" stroke-width="4" stroke-linecap="round" stroke-linejoin="round"/>

      <!-- y axis values -->
      <line x1="84" y1="44" x2="142" y2="44" stroke="var(--grid)" stroke-width="1"/>
      <line x1="84" y1="220" x2="142" y2="220" stroke="var(--grid)" stroke-width="1"/>
      <line x1="84" y1="404" x2="142" y2="404" stroke="var(--grid)" stroke-width="1"/>
      <text class="serif axis-value" x="84" y="40">15€</text>
      <text class="serif axis-value" x="84" y="216">10€</text>
      <text class="serif axis-value" x="84" y="400">5€</text>
      <text class="serif axis-title" transform="translate(140 305) rotate(-90)" text-anchor="middle">Effektivmiete je m²</text>

      <!-- x axis values -->
      <text class="serif axis-title" x="244" y="425">Gesamtmiete</text>
      <text class="serif axis-value" x="155" y="447">5<tspan class="axis-unit">mio</tspan> €</text>
      <text class="serif axis-value" x="470" y="447">10<tspan class="axis-unit">mio</tspan> €</text>
      <text class="serif axis-value" x="799" y="447">15<tspan class="axis-unit">mio</tspan> €</text>

      <!-- legend -->
      <circle cx="570" cy="40" r="13" fill="var(--bubble-soft)" stroke="var(--ink)" stroke-width="2"/>
      <rect x="565" y="36" width="10" height="10" fill="var(--ink)" opacity="0.5"/>
      <text class="serif legend-text" x="594" y="44">Die Größe der Blasen zeigt die Objektgröße an.</text>

      <!-- info data sheet -->
      <rect x="187" y="144" width="109" height="98" rx="5" fill="url(#info-fill)" stroke="var(--ink)" stroke-width="2.5"/>
      <rect x="188" y="131" width="46" height="16" fill="var(--sheet)"/>
      <text class="serif info-title" x="193" y="144">Info</text>
      <g class="serif info-text" text-anchor="middle">
        <text x="241" y="162">Effektivmiete</text>
        <text x="241" y="173">20.30€</text>
        <text x="241" y="191">Gesamtmiete</text>
        <text x="241" y="202">8mio€</text>
        <text x="241" y="220">Größe</text>
        <text x="241" y="231">8000m²</text>
      </g>

      <!-- trend arrows -->
      <path class="trend-arrow" d="M375,336 Q400,330 410,305" marker-end="url(#arrow-head)"/>
      <path class="trend-arrow" d="M432,208 Q436,196 450,192" marker-end="url(#arrow-head)"/>
      <path class="trend-arrow" d="M548,282 Q570,278 575,257" marker-end="url(#arrow-head)"/>

      <!-- bubble 01 -->
      <g class="bubble">
        <circle class="bubble-fill" cx="340" cy="286" r="41" role="img" aria-label="Gebäude-Illustration Objekt 01"/>
        <circle class="bubble-ring" cx="337" cy="288" r="46" pathLength="100"/>
        <text class="bubble-number" x="317" y="276">01</text>
      </g>
      <!-- bubble 02 -->
      <g class="bubble">
        <circle class="bubble-fill" cx="429" cy="254" r="33" role="img" aria-label="Gebäude-Illustration Objekt 02"/>
        <circle class="bubble-ring" cx="426" cy="256" r="38" pathLength="100"/>
        <text class="bubble-number" x="408" y="245">02</text>
      </g>
      <!-- bubble 03 -->
      <g class="bubble">
        <circle class="bubble-fill" cx="498" cy="224" r="44" role="img" aria-label="Gebäude-Illustration Objekt 03"/>
        <circle class="bubble-ring" cx="495" cy="226" r="49" pathLength="100"/>
        <text class="bubble-number" x="474" y="213">03</text>
      </g>
      <!-- bubble 04 -->
      <g class="bubble">
        <circle class="bubble-fill" cx="632" cy="207" r="56" role="img" aria-label="Hochhaus-Illustration Objekt 04"/>
        <circle class="bubble-ring" cx="628" cy="210" r="62" pathLength="100"/>
        <text class="bubble-number" x="604" y="188">04</text>
      </g>
    </svg>
  </div>
</div>
</body>
</html>
```